Derek Folsom Resume

Need to update resume with latest position and ensure it stays to 2 pages, may need advice on what to get rid of and simply clean it up, already have a format that i like but am open to change but don't want to spend a fortune

```html
<!DOCTYPE html>
<html lang="en">
<head>
<meta charset="utf-8">
<title>Derek Folsom Resume</title>
<link href="https://fonts.googleapis.com/css2?family=Josefin+Sans:wght@300;400;600&display=swap" rel="stylesheet">
<style>
:root{
  --ink:#111111;
  --paper:#ffffff;
  --band:#000000;
  --band-text:#ffffff;
  --body:#2a2a2a;
}
*{margin:0;padding:0;box-sizing:border-box}
html,body{width:849px;height:1200px;overflow:hidden;background:var(--paper)}
body{font-family:"Josefin Sans",sans-serif;color:var(--body)}
.resume{position:relative;width:849px;height:1200px;overflow:hidden}
.sidebar{position:absolute;left:0;top:0;width:249px;height:1200px;background:var(--band);color:var(--band-text)}
.trait{position:absolute;left:0;width:249px;text-align:center;font-weight:400;line-height:1}
.trait--caps{text-transform:uppercase}
.trait--sc{font-variant:small-caps}
.trait-sub{display:block;font-size:14px;font-variant:small-caps;margin-top:3px;letter-spacing:.5px}
.name{position:absolute;left:381px;top:26px;font-size:52px;font-weight:400;font-variant:small-caps;color:var(--ink);letter-spacing:2px;line-height:1}
.contact{position:absolute;left:382px;top:84px;font-size:13.5px;color:var(--ink)}
.section{position:absolute;left:295px;width:505px}
.section-head{display:flex;align-items:center;height:22px}
.marker{width:69px;height:19px;flex:none}
.section-title{margin-left:17px;font-size:20px;font-weight:400;font-variant:small-caps;color:var(--ink);letter-spacing:.5px}
.section-body{margin-left:86px;margin-top:3px;font-size:10.4px;line-height:12.6px;font-variant:small-caps;text-align:justify;color:var(--body)}
.section-body p{margin-bottom:5px}
.section-body p.tight{margin-bottom:0}
.role{text-decoration:underline;margin-bottom:6px!important}
.year{position:absolute;left:306px;font-size:19px;font-weight:300;color:var(--ink)}
</style>
</head>
<body>
<div class="resume">
  <aside class="sidebar">
    <div class="trait trait--caps" style="top:147px;font-size:24px;letter-spacing:1px">Knowledge</div>
    <div class="trait trait--caps" style="top:306px;font-size:44px;font-weight:300;letter-spacing:1px">Loyal</div>
    <div class="trait trait--sc" style="top:443px;font-size:34px">Aggressive<span class="trait-sub">energetic sales leader</span></div>
    <div class="trait trait--caps" style="top:579px;font-size:17px;letter-spacing:.8px">Analytical skills</div>
    <div class="trait trait--caps" style="top:709px;font-size:17px;letter-spacing:.8px">Consultative sales</div>
    <div class="trait trait--caps" style="top:860px;font-size:46px;font-weight:300;letter-spacing:1px">Trust</div>
    <div class="trait trait--caps" style="top:991px;font-size:17px;letter-spacing:.8px">Communication</div>
  </aside>

  <h1 class="name">Derek Folsom</h1>
  <div class="contact">555.010.4421 / derekfolsom@mailpost.net / 1187 Larkspur Court</div>

  <section class="section" style="top:122px">
    <div class="section-head"><svg class="marker" viewBox="0 0 69 19"><polygon points="0,0 61,0 69,9.5 61,19 0,19" fill="#000"/></svg><h2 class="section-title">About me</h2></div>
    <div class="section-body">
      <p class="tight">Aggressive, loyal, energetic sales leader with a history of turning around underperforming teams, departments, and territories. Proven consultative sales approach with a focus on product knowledge, trust, and superior service. Strong interpersonal, communication, presentation, and analytical skills.</p>
      <p class="tight">- Developed effective sales incentives and initiatives that became company-wide best practices.</p>
      <p class="tight">- Drove revenue growth at direct, indirect, and retail sales levels; won multiple prestigious awards.</p>
      <p class="tight">- Recruited, developed, trained, and motivated high-energy sales/customer support teams.</p>
    </div>
  </section>

  <section class="section" style="top:302px">
    <div class="section-head"><svg class="marker" viewBox="0 0 69 19"><polygon points="0,0 61,0 69,9.5 61,19 0,19" fill="#000"/></svg><h2 class="section-title">core competencies include</h2></div>
    <div class="section-body">
      <p class="tight">New Business Development | C-Level Relationship Building | Complex Solution Selling High-Impact Sales Presentations | B2C &amp; B2B Channels | Machine to Machine Technology Channel Manager | Performance Management | Competitive Analysis | CRM Territory Sales Management | SaaS | Budgeting &amp; Forecasting | Vendor Management</p>
    </div>
  </section>

  <section class="section" style="top:409px">
    <div class="section-head"><svg class="marker" viewBox="0 0 69 19"><polygon points="0,0 61,0 69,9.5 61,19 0,19" fill="#000"/></svg><h2 class="section-title">Awards - Winning Sales Manager</h2></div>
    <div class="section-body">
      <p class="tight">Driving exceptional levels of sales results in competitive industries and changing environments.</p>
    </div>
  </section>

  <section class="section" style="top:473px">
    <div class="section-head"><svg class="marker" viewBox="0 0 69 19"><polygon points="0,0 61,0 69,9.5 61,19 0,19" fill="#000"/></svg><h2 class="section-title">Career Present</h2></div>
    <div class="section-body">
      <p class="role">Veltrona 2014 - Developmental Executive</p>
      <p>Sell wireless portfolio to the Department of Defense, Department of Homeland Security, Department of Justice, Hallworth Mercer, and Aerovance.</p>
      <p>Increased overall revenue in assigned agencies 101.8% YOY.</p>
      <p class="tight">- Wireless Solutions: Facilitate critical communications for U.S. federal government through wireless solutions for networks, infrastructures, and security and surveillance.</p>
      <p class="tight">- Government Contracts: Navigate complex matrix of budgeting, bidding, and procurement for government contracts.</p>
      <p class="tight">- Collaboration: Work closely with solution engineers, project managers, and C-level executives on identifying the best solutions for their organizations.</p>
    </div>
  </section>

  <section class="section" style="top:681px">
    <div class="section-head"><svg class="marker" viewBox="0 0 69 19"><polygon points="0,0 61,0 69,9.5 61,19 0,19" fill="#000"/></svg><h2 class="section-title">Career History</h2></div>
    <div class="section-body">
      <p class="role">Corvane Networks 2014 - Client Business Manager</p>
      <p>Held national responsibility for sales of the entire Corvane solutions portfolio to the Federal Reserve. Solutions included mobility, professional services, IP, Cloud, SaaS, Network Infrastructure, and Managed Solutions.</p>
      <p>Sold nationwide managed Wi-Fi solution for all 12 Federal Reserve Bank locations.</p>
      <p class="tight">- Complex Negotiations: Renewed three major contracts resulting in annual revenue of $12 million dollars.</p>
      <p class="tight">- Partner Relationships: Worked closely with system integrators, distributors, and value-added resellers.</p>
      <p>- Strategic Planning: Created strong nationwide strategic sales programs targeted to the Federal Reserve.</p>
      <p class="role" style="margin-top:10px">Stridelink 2012 -2014 - Client Executive</p>
      <p>Managed all aspects of national account management including establishing C-level communications, negotiating contracts, selling complex solutions, and increasing revenue and product penetration. Responsible for Homeland Security, Department of Justice, Capitol Hill, and Department of Education.</p>
      <p>Sold largest Mobile solution in Stridelink History - 10K smartphones across Homeland Security within a 6-month timeframe.</p>
      <p class="tight">- Sales Recognition: Received 2012 President's Circle Honor due to finishing 2012 at 133% to budget.</p>
      <p class="tight">- Revenue Growth: Consistently overachieved monthly revenue quota.</p>
      <p class="tight">- Market Share: Negotiated multimillion, multiyear contracts to ensure financial contracts were secured in order to provide opportunities for Regional Account Managers to sell within local market.</p>
      <p class="tight">- Solution Selling: Responsible for selling entire portfolio including IaaS, SaaS, SIP, MPLS, and Wireless.</p>
      <p class="tight">- Training &amp; Leadership: Developed, disseminated, and provided training on national programs to Stridelink's field account managers; offered valuable insight by creating a bi-weekly agency newsletter, which outlined potential gaps and needs.</p>
    </div>
  </section>

  <div class="year" style="top:795px">2014</div>
  <div class="year" style="top:1010px">2012</div>
</div>
</body>
</html>
```